Boutique town planning business needs a Business Card design

We need a business card design for a new company called The Zoning Bridgeway. We provide town planning and urban design services to government, business and community groups. We would like to see the designs use the colours in the logo (blue, deep red, green and amber), plenty of white and including black and grey in the writing. The final design should communicate collaboration, creativity and professionalism and that we are approachable.

```html
<!DOCTYPE html>
<html lang="en">
<head>
<meta charset="utf-8">
<title>The Zoning Bridgeway – Business Card</title>
<link rel="stylesheet" href="https://fonts.googleapis.com/css2?family=Open+Sans:wght@400;600;700&display=swap">
<style>
  :root {
    --red: #b0302a;
    --blue: #1396be;
    --amber: #f0961f;
    --green: #5aa646;
    --ink: #2b2b2b;
    --grey: #8f8f93;
    --light-grey: #c9c9cc;
    --paper: #ffffff;
    --stage: #e6e4e1;
  }
  * { box-sizing: border-box; margin: 0; padding: 0; }
  html, body { width: 1200px; height: 800px; overflow: hidden; }
  body {
    background: var(--stage);
    font-family: "Open Sans", Arial, sans-serif;
    position: relative;
  }

  /* Back of card */
  .card-back {
    position: absolute;
    left: 120px; top: 130px;
    width: 340px; height: 540px;
    background: var(--paper);
    padding: 8px;
    display: grid;
    grid-template-columns: 1fr 1fr;
    grid-template-rows: 1fr 1fr;
    gap: 8px;
    box-shadow: 0 6px 18px rgba(0,0,0,.18);
  }
  .panel--red { background: var(--red); }
  .panel--blue { background: var(--blue); }
  .panel--amber { background: var(--amber); }
  .panel--green { background: var(--green); }

  /* Front of card */
  .card-front {
    position: absolute;
    left: 520px; top: 212px;
    width: 620px; height: 376px;
    background: var(--paper);
    box-shadow: 0 6px 18px rgba(0,0,0,.18);
    overflow: hidden;
  }
  .brand {
    position: absolute;
    left: 40px; top: 36px;
    display: flex; align-items: center; gap: 14px;
  }
  .brand__dot {
    width: 44px; height: 44px; border-radius: 50%;
    background: var(--blue);
  }
  .brand__name {
    font-weight: 700; font-size: 24px; color: var(--ink);
    letter-spacing: -0.2px;
  }
  .rule {
    position: absolute;
    left: 40px; right: 40px; top: 104px;
    height: 5px;
    display: flex;
  }
  .rule span { height: 100%; }
  .rule .seg-green { flex: 4; background: var(--green); }
  .rule .seg-grey { flex: 2; background: var(--grey); }
  .rule .seg-light { flex: 2; background: var(--light-grey); }
  .rule .seg-black { flex: 2; background: var(--ink); }

  .contact {
    position: absolute;
    left: 40px; top: 136px;
    list-style: none;
    font-size: 15px; color: var(--ink);
    line-height: 26px;
  }
  .contact li { display: flex; align-items: center; gap: 10px; white-space: nowrap; }
  .contact svg { width: 14px; height: 14px; flex: none; }

  .person {
    position: absolute;
    right: 40px; top: 136px;
    text-align: right;
  }
  .person__name { font-size: 24px; font-weight: 600; color: var(--blue); }
  .person__credentials { font-size: 11px; color: var(--blue); margin-top: 2px; white-space: nowrap; }
  .person__role { font-size: 16px; color: var(--ink); margin-top: 2px; }
  .abn {
    position: absolute;
    right: 40px; top: 250px;
    font-size: 19px; color: var(--green);
  }

  .swatches {
    position: absolute;
    right: 0; bottom: 0;
    display: flex;
  }
  .swatches span { width: 64px; height: 40px; }
  .swatches .sw-green { background: var(--green); }
  .swatches .sw-amber { background: var(--amber); }
  .swatches .sw-red { background: var(--red); }
  .swatches .sw-blue { background: var(--blue); }
</style>
</head>
<body>
  <section class="card-back" aria-label="Business card reverse">
    <div class="panel panel--red"></div>
    <div class="panel panel--blue"></div>
    <div class="panel panel--amber"></div>
    <div class="panel panel--green"></div>
  </section>

  <section class="card-front" aria-label="Business card front">
    <div class="brand">
      <span class="brand__dot"></span>
      <span class="brand__name">The Zoning Bridgeway</span>
    </div>

    <div class="rule">
      <span class="seg-green"></span><span class="seg-grey"></span><span class="seg-light"></span><span class="seg-black"></span>
    </div>

    <ul class="contact">
      <li>
        <svg viewBox="0 0 14 14" aria-hidden="true"><rect x="3.5" y="1" width="7" height="12" rx="1.5" fill="none" stroke="#f0961f" stroke-width="1.4"/><circle cx="7" cy="10.8" r="0.8" fill="#f0961f"/></svg>
        0412 555 018
      </li>
      <li>
        <svg viewBox="0 0 14 14" aria-hidden="true"><rect x="1" y="3" width="12" height="8" rx="1" fill="#f0961f"/><path d="M1.5 3.5 L7 8 L12.5 3.5" fill="none" stroke="#fff" stroke-width="1.2"/></svg>
        studio@zoningbridgeway.com.au
      </li>
      <li>
        <svg viewBox="0 0 14 14" aria-hidden="true"><circle cx="7" cy="7" r="5.8" fill="none" stroke="#f0961f" stroke-width="1.3"/><ellipse cx="7" cy="7" rx="2.5" ry="5.8" fill="none" stroke="#f0961f" stroke-width="1"/><line x1="1.2" y1="7" x2="12.8" y2="7" stroke="#f0961f" stroke-width="1"/></svg>
        www.zoningbridgeway.com.au
      </li>
    </ul>

    <div class="person">
      <p class="person__name">Miriam Ashdown</p>
      <p class="person__credentials">BUrbDes (Town Studies), MPlan, RPTA, LGPA</p>
      <p class="person__role">Director</p>
    </div>

    <p class="abn">ABN 51824753556</p>

    <div class="swatches" aria-hidden="true">
      <span class="sw-green"></span><span class="sw-amber"></span><span class="sw-red"></span><span class="sw-blue"></span>
    </div>
  </section>
</body>
</html>
```